Chauffeur Car Driver Needing a design with/without logo for business cards

I'm a chauffeur car driver in Melbourne Australia. I have an extensive list of personal customers and need to provide a professional business card to new customers.
My business name is 'RidgeMark'.
I offer a personalised service to customer who need a transport alternative to taxis. I don't want it to look too 'upmarket' as i don't want it to seem too expensive or only for special occasions. The majority of my clients are business professionals who use me for airport transfers.
I definitely don't want the card/logo to have an image of a car/road etc. I prefer something abstract. A 'pencil-line'-type font will grab my attention but not absolutely necessary. Not too 'digital' or 'ultra - modern' looking.
I need the card to display the following information
Ridge Mark - main logo/text
Chauffeur Cars - sub text
Bruno Fellisar
0498 271 536
bookings@RidgeMark.com.au
I would like the focus to be on 'RidgeMark' with everything else smaller.
Look forward to seeing ideas!!!!
Target Market(s)
Business Corporate Professionals
Industry/Entity Type
Airport
Requirements
Nice to have
- Pencil line type font
Should not have
- Images of cars, road, tyres, steering wheel etc.

```html
<!DOCTYPE html>
<html lang="en">
<head>
<meta charset="utf-8">
<title>RidgeMark – Business Card</title>
<link rel="stylesheet" href="https://fonts.googleapis.com/css2?family=PT+Sans:wght@400;700&display=swap">
<style>
  :root {
    --ink-blue: #2e3591;
    --deep-blue: #2b338c;
    --lavender: #9a9ccb;
    --soft-lavender: #b7b8da;
    --paper: #ffffff;
  }
  html, body {
    margin: 0;
    padding: 0;
    width: 1200px;
    height: 734px;
    overflow: hidden;
    background: var(--paper);
  }
  .card {
    position: relative;
    width: 1200px;
    height: 734px;
    overflow: hidden;
    background: var(--deep-blue);
    font-family: "PT Sans", "Helvetica Neue", Arial, sans-serif;
  }
  .card__waves {
    position: absolute;
    inset: 0;
    width: 1200px;
    height: 734px;
    display: block;
  }
  .brand-name {
    position: absolute;
    left: 0;
    top: 118px;
    width: 1080px;
    margin: 0;
    text-align: center;
    font-size: 168px;
    font-weight: 700;
    line-height: 1;
    letter-spacing: 2px;
    color: var(--ink-blue);
  }
  .contact {
    position: absolute;
    right: 92px;
    top: 498px;
    margin: 0;
    text-align: right;
    color: var(--paper);
    font-size: 35px;
    font-weight: 400;
    line-height: 50px;
  }
  .contact__line {
    display: block;
  }
</style>
</head>
<body>
  <main class="card">
    <svg class="card__waves" viewBox="0 0 1200 734" aria-hidden="true">
      <defs>
        <linearGradient id="lowerSweep" x1="0" y1="1" x2="1" y2="0">
          <stop offset="0" stop-color="#a4a6d2"/>
          <stop offset="0.55" stop-color="#3f469a"/>
          <stop offset="1" stop-color="#2b338c"/>
        </linearGradient>
        <linearGradient id="edgeGlow" x1="0" y1="0" x2="1" y2="1">
          <stop offset="0" stop-color="#6b6fb3"/>
          <stop offset="0.5" stop-color="#c3c4e2"/>
          <stop offset="1" stop-color="#4d539f"/>
        </linearGradient>
      </defs>

      <!-- lower-left lighter sweep -->
      <path d="M0 734 L0 590 C220 520 520 500 760 492 C930 486 1060 470 1200 420 L1200 734 Z" fill="url(#lowerSweep)"/>

      <!-- dark band beneath the white field -->
      <path d="M0 590 C220 520 520 500 760 492 C930 486 1060 470 1200 420 L1200 390 C1100 440 1000 440 900 430 C700 410 420 430 0 480 Z" fill="var(--deep-blue)"/>

      <!-- soft lavender edge along the right of the white field -->
      <path d="M930 0 L1000 0 C1090 60 1110 190 1095 290 C1080 380 1010 430 930 440 C1000 400 1050 330 1060 250 C1070 150 1030 60 930 0 Z" fill="url(#edgeGlow)" opacity="0.85"/>

      <!-- white field -->
      <path d="M0 0 L940 0 C1030 50 1075 150 1062 255 C1050 340 990 400 900 408 C760 418 560 395 380 410 C230 422 100 455 0 510 Z" fill="var(--paper)"/>
    </svg>

    <h1 class="brand-name">RidgeMark</h1>

    <p class="contact">
      <span class="contact__line contact__tagline">Chauffeur Cars - sub text</span>
      <span class="contact__line contact__person">Bruno Fellisar</span>
      <span class="contact__line contact__phone">0498 271 536</span>
      <span class="contact__line contact__email">bookings@RidgeMark.com.au</span>
    </p>
  </main>
</body>
</html>
```